Microlight Aircraft Website Project

Need a website designed, or at least a template made, that my web programmer can work with here. We are a new manufacturer of microlight aircraft & powered hang gliders. Our company name is Bright Fern. We manufacture portable utility aircraft in the Light Sport category (formerly known as Ultralights or Microlights). Our particular design is a 2-seat powered hang glider and caters to those who want to go explore the backcountry. We are not necessarily aviation nuts, but more into the development of a flying utility vehicle for extreme exploration and expeditions. We have been importing these aircraft from 3 countries for 15 years and have supplied over 200 expedition-quality aircraft world-wide. We are now manufacturing here in the US.

Industry/Entity Type

Manufacturer

Coding

Coded - Design and coding required

```html
<!DOCTYPE html>
<html lang="en">
<head>
<meta charset="utf-8">
<title>Bright Fern – Microlight Aircraft &amp; Powered Hang Gliders</title>
<link rel="stylesheet" href="https://fonts.googleapis.com/css2?family=Raleway:wght@400;600;700;800&family=Lato:wght@400;700&display=swap">
<style>
:root{
  --blue:#0a5fb0;
  --blue-bright:#1a8fd8;
  --blue-light:#35a8e6;
  --navy:#063a7c;
  --navy-deep:#042f68;
  --ink:#2b2b2b;
  --grey:#8a8a8a;
  --line:#dcdcdc;
  --sky-top:#cfe3f4;
  --sky-bottom:#eef5fb;
  --white:#ffffff;
}
*{box-sizing:border-box;margin:0;padding:0}
html,body{width:1200px;height:2244px;overflow:hidden}
body{font-family:'Lato',Arial,sans-serif;color:var(--ink);background:var(--white)}
.page{position:relative;width:1200px;height:2244px;overflow:hidden}
.abs{position:absolute}

/* header */
.site-header{left:0;top:0;width:1200px;height:102px;background:linear-gradient(#f4f8fc,#e4eef8);border-top:3px solid var(--blue-bright)}
.brand{left:160px;top:22px;display:flex;align-items:center;gap:10px}
.brand-dot{width:30px;height:30px;border-radius:50%;background:var(--blue)}
.brand-name{font-family:'Raleway',Arial,sans-serif;font-weight:800;font-size:24px;color:var(--blue);letter-spacing:.5px}
.top-cta{right:0;top:0;height:32px;display:flex}
.top-phone{background:var(--blue-light);color:var(--white);font-family:'Raleway',Arial,sans-serif;font-weight:700;font-size:16px;display:flex;align-items:center;gap:8px;padding:0 14px 0 16px;clip-path:polygon(10px 0,100% 0,100% 100%,0 100%)}
.top-consult{background:var(--navy);color:var(--white);font-family:'Lato',Arial,sans-serif;font-weight:700;font-size:14px;display:flex;align-items:center;padding:0 20px 0 12px;width:170px;margin-right:135px;clip-path:polygon(0 0,100% 0,calc(100% - 10px) 100%,0 100%)}
.main-nav{left:466px;top:66px;display:flex;align-items:center;font-family:'Raleway',Arial,sans-serif;font-weight:700;font-size:13px;color:#1c1c1c}
.main-nav a{color:inherit;text-decoration:none;padding:0 16px;border-left:1px solid #c9d4df;line-height:14px}
.main-nav a:first-child{border-left:none;padding-left:0}

/* hero */
.hero{left:0;top:102px;width:1200px;height:483px;background:linear-gradient(100deg,#a8262a 0%,#6b3a33 28%,#5f7a86 48%,#9fb3bf 65%,#4f6a3e 82%,#3e5a2c 100%)}
.hero-title{left:698px;top:152px;width:420px;font-family:'Raleway',Arial,sans-serif;font-weight:700;font-size:31px;line-height:42px;color:var(--white);text-shadow:0 1px 3px rgba(0,0,0,.4)}
.hero-arrow{top:328px}
.hero-dots{left:571px;top:541px;display:flex;gap:8px}
.hero-dots span{width:12px;height:12px;border-radius:50%;background:var(--white)}
.hero-dots span.active{background:var(--blue-bright);border:2px solid var(--white)}

/* welcome */
.welcome{left:0;top:585px;width:1200px;height:355px;background:linear-gradient(var(--sky-top),var(--sky-bottom) 35%,#f7fbfe)}
.section-title{font-family:'Raleway',Arial,sans-serif;font-weight:400;font-size:34px;color:#2a2a2a;text-align:center;letter-spacing:.3px}
.section-title b{font-weight:800}
.welcome .section-title{position:absolute;left:0;width:1200px;top:65px}
.title-rule{left:280px;top:125px;width:640px;height:20px}
.welcome-text{left:195px;top:157px;width:810px;font-size:11.5px;line-height:22px;color:#333;text-align:center}
.btn{display:inline-block;background:linear-gradient(var(--blue-bright),var(--blue));color:var(--white);font-family:'Raleway',Arial,sans-serif;font-weight:700;font-size:11px;text-transform:uppercase;letter-spacing:.4px;border-radius:2px;text-align:center}
.welcome .btn{position:absolute;left:548px;top:266px;width:104px;height:32px;line-height:32px}

/* manufacture */
.manufacture{left:0;top:940px;width:1200px;height:450px;background:linear-gradient(180deg,#2d3d5c 0%,#3a4b63 40%,#4a5538 75%,#3d3d2e 100%)}
.manufacture .section-title{position:absolute;left:0;width:1200px;top:44px;color:var(--white)}
.tab{top:110px;width:426px;height:55px;border:1px solid rgba(255,255,255,.6);background:rgba(20,28,40,.78);display:flex;align-items:center;justify-content:center;gap:14px;color:var(--white);font-family:'Raleway',Arial,sans-serif;font-size:21px}
.tab.active::after{content:"";position:absolute;left:50%;bottom:-12px;margin-left:-12px;border:12px solid transparent;border-top-color:rgba(255,255,255,.85);border-bottom:none}
.tab-underline{position:absolute;left:66px;right:66px;bottom:0;height:3px;background:var(--white)}
.product{top:193px;width:211px;height:197px;background:var(--white);padding:6px}
.product-photo{width:199px;height:134px}
.product-name{position:absolute;left:0;bottom:0;width:211px;height:50px;background:linear-gradient(var(--blue-light),var(--blue));color:var(--white);font-family:'Raleway',Arial,sans-serif;font-size:21px;line-height:50px;text-align:center}
.slide-arrow{top:262px}

/* news & events */
.news-block{top:1444px}
.block-title{font-family:'Raleway',Arial,sans-serif;font-size:22px;color:#222;letter-spacing:.3px}
.block-title b{font-weight:800}
.read-all{position:absolute;right:0;top:10px;font-family:'Raleway',Arial,sans-serif;font-weight:700;font-size:9px;color:var(--blue-bright)}
.block-rule{position:absolute;left:0;right:0;top:36px;height:1px;background:var(--line)}
.item{position:absolute;left:0;right:0}
.news-thumb{position:absolute;left:0;top:0;width:90px;height:93px;background:linear-gradient(160deg,#e7eef6 0%,#3a4a6a 45%,#6b7a3a 80%,#a03a2a 100%)}
.event-thumb{position:absolute;left:0;top:0;width:83px;height:52px;background:linear-gradient(180deg,#2a2a2a 0%,#7a5a30 50%,#c8c0a8 100%)}
.item h3{font-family:'Raleway',Arial,sans-serif;font-weight:700;font-size:12px;color:#222}
.item h3 .date{font-family:'Lato',Arial,sans-serif;font-weight:400;font-style:italic;font-size:10px;color:var(--blue);margin-left:12px}
.item p{font-size:10.5px;line-height:17px;color:#8c8c8c;margin-top:8px}
.item .more{display:block;font-family:'Raleway',Arial,sans-serif;font-weight:700;font-size:9px;color:var(--blue-bright);margin-top:3px}
.item-rule{position:absolute;left:0;right:0;height:1px;background:var(--line)}
.col-divider{left:599px;top:1440px;width:1px;height:300px;background:#ececec}

/* subscribe */
.subscribe-band{left:0;top:1790px;width:1200px;height:190px;background:linear-gradient(180deg,#9cc3e4 0%,#cfe2f2 45%,#e9f2fa 100%)}
.subscribe-box{left:240px;top:1843px;width:750px;height:95px;background:var(--white);box-shadow:0 3px 6px rgba(0,0,0,.2);border-top:5px solid transparent;border-image:repeating-linear-gradient(135deg,var(--navy) 0 10px,var(--white) 10px 16px,var(--blue-light) 16px 26px,var(--white) 26px 32px) 5}
.subscribe-head{left:73px;top:25px;font-family:'Raleway',Arial,sans-serif;color:#333;line-height:20px}
.subscribe-head strong{display:block;font-weight:800;font-size:18px}
.subscribe-head span{font-size:17px}
.social{left:255px;top:32px;display:flex;gap:11px}
.social span{width:22px;height:22px;border-radius:50%}
.email-field{left:372px;top:28px;width:233px;height:32px;border:1px solid #d6d6d6;font-size:10px;color:#999;padding:0 10px;line-height:30px}
.subscribe-box .btn{position:absolute;left:622px;top:28px;width:109px;height:32px;line-height:32px;font-size:10.5px}

/* footer */
.site-footer{left:0;top:1980px;width:1200px;height:264px;background:var(--navy)}
.foot-col{top:42px}
.foot-title{font-family:'Raleway',Arial,sans-serif;font-weight:700;font-size:14px;color:var(--white);padding-bottom:10px;border-bottom:1px solid rgba(255,255,255,.25)}
.foot-links{list-style:none;margin-top:8px}
.foot-links li{font-size:10px;color:#cfe0f2;line-height:20px;padding-left:12px;position:relative}
.foot-links li::before{content:"›";position:absolute;left:0;color:var(--blue-light)}
.field{border:1px solid #3d7ac4;background:var(--navy-deep);color:#cfe0f2;font-size:10px;padding:4px 6px;width:190px;height:22px;margin-top:6px;border-radius:2px}
.field.msg{height:38px}
.foot-btn{display:inline-block;margin-top:9px;background:var(--blue-light);color:var(--white);font-weight:700;font-size:11px;padding:3px 8px;border-radius:2px}
.contact-row{display:flex;gap:10px;font-size:11px;color:#e1ecf8;line-height:16px;margin-top:16px}
.contact-row svg{flex:none;margin-top:2px}
.foot-divider{top:30px;width:1px;height:190px;background:rgba(255,255,255,.15)}
.foot-brand{left:890px;top:32px;width:140px;text-align:center;color:var(--white)}
.foot-brand .brand-dot{width:38px;height:38px;margin:12px auto 10px;background:var(--white)}
.foot-brand .brand-name{color:var(--white);font-size:22px;display:block}
.foot-brand small{display:block;font-weight:700;font-size:10px;line-height:16px;margin-top:8px}
</style>
</head>
<body>
<div class="page">

  <header class="site-header abs">
    <div class="brand abs"><span class="brand-dot"></span><span class="brand-name">BRIGHT FERN</span></div>
    <div class="top-cta abs">
      <div class="top-phone">
        <svg width="16" height="16" viewBox="0 0 16 16"><circle cx="8" cy="8" r="7" fill="none" stroke="#fff" stroke-width="1.4"/><path d="M5.5 4.5l1.4 1.5-.8 1c.5 1 1.3 1.8 2.2 2.3l1-.8 1.5 1.3-.8 1.2C7.8 10.8 5.3 8.3 4.8 5.6z" fill="#fff"/></svg>
        555 014 2270
      </div>
      <div class="top-consult">Get A Free Consultation</div>
    </div>
    <nav class="main-nav abs">
      <a href="#"><svg width="20" height="18" viewBox="0 0 20 18"><path d="M10 1L1 9h3v8h4.5v-5h3v5H16V9h3z" fill="#0a5fb0"/></svg></a>
      <a href="#">ABOUT US</a>
      <a href="#">READY TO FLY</a>
      <a href="#">GALLERY</a>
      <a href="#">DOWNLOADS</a>
      <a href="#">CONTACT US</a>
    </nav>
  </header>

  <section class="hero abs" role="img" aria-label="Photo of two pilots in a red microlight aircraft flying over forested hills">
    <svg class="hero-arrow abs" style="left:88px" width="20" height="44" viewBox="0 0 20 44"><path d="M18 2L3 22l15 20" fill="none" stroke="#fff" stroke-width="2.5"/></svg>
    <h1 class="hero-title abs">MANUFACTURING MICRO LIGHT AIRCRAFT &amp; POWERED HANG GLIDERS</h1>
    <svg class="hero-arrow abs" style="left:1094px" width="20" height="44" viewBox="0 0 20 44"><path d="M2 2l15 20L2 42" fill="none" stroke="#fff" stroke-width="2.5"/></svg>
    <div class="hero-dots abs"><span class="active"></span><span></span><span></span></div>
  </section>

  <section class="welcome abs">
    <h2 class="section-title">WELCOME TO <b>BRIGHT FERN</b></h2>
    <svg class="title-rule abs" viewBox="0 0 640 20"><line x1="0" y1="10" x2="295" y2="10" stroke="#b8c6d4"/><line x1="345" y1="10" x2="640" y2="10" stroke="#b8c6d4"/><circle cx="320" cy="10" r="9" fill="#0a5fb0"/></svg>
    <p class="welcome-text abs">Lorem ipsum dolor sit amet, consectetuer adipiscing elit, sed diam nonummy nibh euismod tincidunt ut laoreet dolore magna aliquam erat volutpat. Ut wisi enim ad minim veniam, quis nostrud exerci tation ullamcorper suscipit lobortis nisl ut aliquip ex ea commodo consequat. Duis autem vel eum iriure dolor in hendrerit in vulputate velit esse molestie consequat, vel illum dolore eu feugiat nulla facilisis at vero eros et accumsan et iusto odio dignissim qui blandit praesent luptatum zzril delenit augue duis dolore te feugait nulla facilisi.</p>
    <a class="btn" href="#">Read More</a>
  </section>

  <section class="manufacture abs" role="img" aria-label="Background photo of a powered hang glider wing above a valley">
    <h2 class="section-title">WE <b>MANUFACTURE</b></h2>
    <div class="tab active abs" style="left:162px">
      <svg width="30" height="24" viewBox="0 0 30 24"><path d="M2 12h26l-2-2H18L11 2H8l4 8H5L3 7H1l1 5-1 5h2l2-3h7l-4 8h3l7-8h8l2-2z" fill="#35a8e6"/></svg>
      MICRO LIGHT AIRCRAFT
      <span class="tab-underline"></span>
    </div>
    <div class="tab abs" style="left:611px">
      <svg width="32" height="20" viewBox="0 0 32 20"><path d="M1 4L31 2 20 10z" fill="#35a8e6"/><path d="M16 8v9M12 17h8" stroke="#35a8e6" stroke-width="2"/></svg>
      POWERED HANG GLIDERS
    </div>
    <svg class="slide-arrow abs" style="left:84px" width="20" height="46" viewBox="0 0 20 46"><path d="M18 2L3 23l15 21" fill="none" stroke="#fff" stroke-width="2"/></svg>
    <div class="product abs" style="left:162px"><div class="product-photo" role="img" aria-label="Photo of a white microlight aircraft over green fields" style="background:linear-gradient(160deg,#5c7a3c,#9aa98a 60%,#c9cfc6)"></div><div class="product-name">TR 500</div></div>
    <div class="product abs" style="left:384px"><div class="product-photo" role="img" aria-label="Photo of a trike microlight against blue sky" style="background:linear-gradient(180deg,#3f7fc4,#6ea5db)"></div><div class="product-name">SPORTS 2S</div></div>
    <div class="product abs" style="left:606px"><div class="product-photo" role="img" aria-label="Photo of a seaplane microlight landing on water" style="background:linear-gradient(180deg,#6b8a99,#2e5168 60%,#d8e2e8)"></div><div class="product-name">WATER SPORTS</div></div>
    <div class="product abs" style="left:828px"><div class="product-photo" role="img" aria-label="Photo of a powered hang glider with purple wing" style="background:linear-gradient(180deg,#6aa6dc,#a9cdee)"></div><div class="product-name">TR 500</div></div>
    <svg class="slide-arrow abs" style="left:1095px" width="20" height="46" viewBox="0 0 20 46"><path d="M2 2l15 21L2 44" fill="none" stroke="#fff" stroke-width="2"/></svg>
  </section>

  <section class="news-block abs" style="left:162px;width:413px">
    <h2 class="block-title">LATEST <b>NEWS</b></h2>
    <span class="read-all">READ ALL »</span>
    <span class="block-rule"></span>
    <article class="item" style="top:52px;height:100px">
      <div class="news-thumb" role="img" aria-label="Photo of a hang glider over a valley"></div>
      <div style="margin-left:105px">
        <h3>Lorem Ipsum Dolor Consecte</h3>
        <p>Sed ut perspiciatis unde omnis iste natus error sit voluptatem accusantium dolo remque laudantium, totam rem aperiam, eaque ipsa quae ab illo inventore veritatis</p>
        <span class="more">READ MORE</span>
      </div>
    </article>
    <span class="item-rule" style="top:164px"></span>
    <article class="item" style="top:180px;height:100px">
      <div class="news-thumb" role="img" aria-label="Photo of a hang glider over a valley"></div>
      <div style="margin-left:105px">
        <h3>Lorem Ipsum Dolor Consecte</h3>
        <p>Sed ut perspiciatis unde omnis iste natus error sit voluptatem accusantium dolo remque laudantium, totam rem aperiam, eaque ipsa quae ab illo inventore veritatis</p>
        <span class="more">READ MORE</span>
      </div>
    </article>
    <span class="item-rule" style="top:292px"></span>
  </section>

  <div class="col-divider abs"></div>

  <section class="news-block abs" style="left:635px;width:408px">
    <h2 class="block-title">UPCOMING <b>EVENTS</b></h2>
    <span class="read-all">READ ALL »</span>
    <span class="block-rule"></span>
    <article class="item" style="top:55px">
      <div class="event-thumb" role="img" aria-label="Photo of a microlight aircraft on an airfield"></div>
      <div style="margin-left:94px"><h3>Lorem Ipsum Dolor Consecte<span class="date">on 29 April, 2016</span></h3><p style="margin-top:4px">Sed ut perspiciatis unde omnis iste natus error sit voluptatem</p><span class="more">READ MORE</span></div>
    </article>
    <span class="item-rule" style="top:122px"></span>
    <article class="item" style="top:136px">
      <div class="event-thumb" role="img" aria-label="Photo of a microlight aircraft on an airfield"></div>
      <div style="margin-left:94px"><h3>Lorem Ipsum Dolor Consecte<span class="date">on 29 April, 2016</span></h3><p style="margin-top:4px">Sed ut perspiciatis unde omnis iste natus error sit voluptatem</p><span class="more">READ MORE</span></div>
    </article>
    <span class="item-rule" style="top:204px"></span>
    <article class="item" style="top:220px">
      <div class="event-thumb" role="img" aria-label="Photo of a microlight aircraft on an airfield"></div>
      <div style="margin-left:94px"><h3>Lorem Ipsum Dolor Consecte<span class="date">on 29 April, 2016</span></h3><p style="margin-top:4px">Sed ut perspiciatis unde omnis iste natus error sit voluptatem</p><span class="more">READ MORE</span></div>
    </article>
    <span class="item-rule" style="top:290px"></span>
  </section>

  <section class="subscribe-band abs"></section>
  <div class="subscribe-box abs">
    <svg class="abs" style="left:0;top:20px" width="62" height="62" viewBox="0 0 62 62"><g fill="none" stroke="#d8d8d8" stroke-width="2"><path d="M4 18L44 4l14 38-40 14z"/><path d="M4 18l30 14L44 4"/></g></svg>
    <div class="subscribe-head abs"><strong>SUBSCRIBE</strong><span>for Latest News</span></div>
    <div class="social abs"><span style="background:#3b5998"></span><span style="background:#1da1f2"></span><span style="background:#dd4b39"></span></div>
    <div class="email-field abs">Enter email address</div>
    <a class="btn" href="#">Subscribe</a>
  </div>

  <footer class="site-footer abs">
    <div class="foot-col abs" style="left:162px;width:108px">
      <h4 class="foot-title">QUICK LINKS</h4>
      <ul class="foot-links"><li>HOME</li><li>ABOUT US</li><li>READY TO FLY</li><li>GALLERY</li><li>DOWNLOADS</li><li>CONTACT US</li></ul>
    </div>
    <div class="foot-divider abs" style="left:307px"></div>
    <div class="foot-col abs" style="left:348px;width:192px">
      <h4 class="foot-title">QUICK INQUIRY</h4>
      <div class="field">Name</div>
      <div class="field">Email</div>
      <div class="field msg">Message</div>
      <span class="foot-btn">Submit</span>
    </div>
    <div class="foot-divider abs" style="left:578px"></div>
    <div class="foot-col abs" style="left:618px;width:200px">
      <h4 class="foot-title">CONTACT DETAILS</h4>
      <div class="contact-row"><svg width="9" height="13" viewBox="0 0 9 13"><path d="M4.5 0A4.5 4.5 0 000 4.5C0 8 4.5 13 4.5 13S9 8 9 4.5A4.5 4.5 0 004.5 0zm0 6.3a1.8 1.8 0 110-3.6 1.8 1.8 0 010 3.6z" fill="#35a8e6"/></svg><span>Bright Fern, 48 Ridgeline Way, Suite 12, Cedar Hollow, Maple County</span></div>
      <div class="contact-row" style="font-weight:700"><svg width="11" height="11" viewBox="0 0 11 11"><path d="M2 0l2 2.5-1 1.4c.7 1.5 1.9 2.7 3.3 3.4l1.3-1L11 8.3 9.6 10.6C4.8 10 .5 5.9 0 1.2z" fill="#35a8e6"/></svg><span>555 - 014 - 2270</span></div>
      <div class="contact-row"><svg width="11" height="8" viewBox="0 0 11 8"><rect width="11" height="8" fill="#35a8e6"/><path d="M0 0l5.5 4.5L11 0" fill="none" stroke="#063a7c"/></svg><span>info@brightfern.com</span></div>
    </div>
    <div class="foot-divider abs" style="left:857px"></div>
    <div class="foot-brand abs">
      <span class="brand-dot"></span>
      <span class="brand-name">BRIGHT FERN</span>
      <small>Copyright © 2016 BRIGHT FERN.<br>All Right Reserved.</small>
    </div>
  </footer>

</div>
</body>
</html>
```